Construction Website Design for Wordpress

Update:
I like this theme as a starting point. It seems like a very good start. Fonts, colors, motion, etc. https://consultancy.qrvistaweb.com/
***************************************************************************************

I want a new website design that can be implemented in wordpress. Here is my existing site: www.halvornquantax.com
Attached is a document with the copy, requirements, sample images, etc. Let me know what questions you have.

Here is a sample of the info, but review the attached document for everything:

Website layout:
Title Bar
• Home
• Expertise
• Takeoffs
• Divisions Serviced (redesign from orig page: (http://www.halvornquantax.com/scope-list/)
• Member Login
Requirements
• Home page has a slider with 3 dimmed commercial construction images and copy overlay
• Request for Proposal Form should be over the slider and the same look and location on every page.
• “Request For Proposal” – No Obligation
o Company Name
o Contact Name
o Contact Phone
o Contact Email
• Use the copy below for the pages
• Split the Client Testimonials among the pages

Target Market(s)

B2B - Construction Companies

Industry/Entity Type

Construction

Number of Pages Required

4 page

Font styles to use
Serif

Colors
0255a3
3276b5
85abd2
d0dfed

Requirements
Must have
• Construction images in slider
• Request for proposal form
• testimonials

```html
<!DOCTYPE html>
<html lang="en">
<head>
<meta charset="utf-8">
<title>Halvorn Quantax – Construction Takeoff Experts</title>
<link href="https://fonts.googleapis.com/css2?family=Montserrat:wght@400;500;600;700&family=Crimson+Text:ital@1&display=swap" rel="stylesheet">
<style>
:root{
  --navy:#0a4f96;
  --navy-deep:#083f7c;
  --sky:#5db9e8;
  --sky-soft:#63bde9;
  --orange:#f0a20c;
  --ink:#2b3440;
  --muted:#6d747c;
  --rule:#d9dee4;
  --white:#ffffff;
}
*{box-sizing:border-box;margin:0;padding:0}
html,body{width:1200px;height:3035px;overflow:hidden}
body{font-family:"Montserrat",sans-serif;color:var(--ink);background:var(--white);position:relative}
a{color:inherit;text-decoration:none}
.abs{position:absolute}

/* header */
.site-header{position:absolute;left:0;top:0;width:1200px;height:75px;background:var(--white)}
.brand{position:absolute;left:122px;top:16px;display:flex;align-items:center;gap:8px}
.brand-dot{width:10px;height:10px;background:var(--sky)}
.brand-name{font-weight:700;font-size:17px;color:var(--navy);letter-spacing:.5px;line-height:1}
.brand-tag{font-size:9px;font-weight:600;color:var(--sky);letter-spacing:.6px;margin-top:4px}
.main-nav{position:absolute;left:472px;top:29px;display:flex;gap:40px;font-size:11px;font-weight:600;letter-spacing:.8px;text-transform:uppercase}
.main-nav .active{color:var(--sky)}
.btn{display:inline-block;background:var(--orange);color:var(--white);font-size:10px;font-weight:700;letter-spacing:1px;text-transform:uppercase;text-align:center}
.login{position:absolute;left:929px;top:21px;width:150px;height:30px;line-height:30px}

/* hero */
.hero{position:absolute;left:0;top:75px;width:1200px;height:450px;background:linear-gradient(180deg,#4f7fb4 0%,#7ea2c8 45%,#9a8a70 78%,#6f5a42 100%)}
.hero-title{position:absolute;left:120px;top:165px;color:var(--white);font-size:34px;font-weight:600;display:flex;align-items:center;gap:18px}
.hero-title::after{content:"";width:44px;height:2px;background:var(--white)}
.hero-sub{position:absolute;left:120px;top:228px;width:600px;color:var(--white);font-size:21px;font-weight:500;line-height:1.45}
.slide-arrow{position:absolute;top:210px}
.quote-form{position:absolute;left:820px;top:60px;width:256px;height:328px;background:var(--white);border:5px solid #d7dde3}
.quote-head{position:absolute;left:-5px;top:-5px;width:256px;height:88px}
.quote-head span{position:absolute;left:0;top:18px;width:256px;text-align:center;color:var(--white);font-size:15px;font-weight:600;line-height:1.1}
.quote-head small{display:block;font-size:10px;font-weight:700;margin-top:3px}
.field{position:absolute;left:28px;width:195px;height:29px;border:1px solid var(--rule);font-size:10px;color:#9aa1a8;padding:8px 6px}
.send{position:absolute;left:71px;top:256px;width:104px;height:28px;line-height:28px;background:var(--sky)}

/* about */
.about-photo{position:absolute;left:120px;top:600px;width:450px;height:339px;background:linear-gradient(180deg,#3d8ee0 0%,#8fc3ef 55%,#b9c7d2 100%)}
.section-title{font-size:20px;font-weight:600;color:var(--navy);display:flex;align-items:center;gap:14px}
.section-title.left::after{content:"";width:38px;height:2px;background:var(--navy)}
.section-title.center{justify-content:center}
.section-title.center::before,.section-title.center::after{content:"";width:40px;height:2px;background:currentColor}
.about-title{position:absolute;left:630px;top:648px}
.about-copy{position:absolute;left:630px;top:688px;width:445px;font-size:11.5px;color:var(--muted);line-height:1.6}
.about-copy p+p{margin-top:16px}
.discover{position:absolute;left:630px;top:866px;width:136px;height:30px;line-height:30px;background:var(--sky)}

/* scopes */
.scopes{position:absolute;left:0;top:1013px;width:1200px;height:624px;background:var(--navy)}
.scopes .section-title{position:absolute;left:0;top:70px;width:1200px;color:var(--white)}
.scope{position:absolute;top:120px;width:219px;color:var(--white)}
.scope-photo{width:219px;height:151px}
.scope h3{font-size:14px;font-weight:600;margin:32px 0 16px}
.scope ul{list-style:none;font-size:10.5px;line-height:1.35;padding-right:30px}
.scope li{position:relative;padding-left:17px;margin-bottom:10px}
.scope li::before{content:"";position:absolute;left:2px;top:3px;width:6px;height:6px;border:1.5px solid var(--white);border-radius:50%}
.scope-link{position:absolute;top:467px;font-size:10px;font-weight:700;letter-spacing:1px;text-transform:uppercase;color:var(--white)}
.all-scopes{position:absolute;left:524px;top:517px;width:151px;height:30px;line-height:30px}

/* takeoffs */
.takeoffs-title{position:absolute;left:0;top:1705px;width:1200px}
.takeoffs-lead{position:absolute;left:385px;top:1745px;width:430px;text-align:center;font-size:11px;color:var(--muted);line-height:1.6}
.step{position:absolute;top:1810px;width:200px;text-align:center}
.step svg{display:block;margin:0 auto}
.step h4{font-size:14px;font-weight:500;color:var(--navy);margin:20px 0 16px}
.step p{font-size:10px;color:var(--muted);line-height:1.6}
.read-more{display:block;margin-top:16px;font-size:10px;font-weight:700;letter-spacing:1px;text-transform:uppercase}

/* testimonial */
.testimonial{position:absolute;left:0;top:2083px;width:1200px;height:329px;background:var(--sky-soft);color:var(--white);text-align:center}
.testimonial blockquote{position:absolute;left:305px;top:52px;width:590px;font-family:"Crimson Text",serif;font-style:italic;font-size:19px;line-height:1.45}
.cite-name{position:absolute;left:0;top:180px;width:1200px;font-size:12px;font-weight:600}
.cite-co{position:absolute;left:0;top:197px;width:1200px;font-size:10px}
.dots{position:absolute;left:563px;top:236px;display:flex;gap:8px}
.dots i{width:9px;height:9px;border:1.5px solid var(--white);border-radius:50%}

/* more */
.more-title{position:absolute;left:0;top:2490px;width:1200px}
.more-copy{position:absolute;left:345px;top:2530px;width:510px;text-align:center;font-size:12px;color:var(--ink);line-height:1.6}
.register{position:absolute;left:532px;top:2604px;width:135px;height:30px;line-height:30px}

/* footer */
.site-footer{position:absolute;left:0;top:2697px;width:1200px;height:338px;background:var(--navy);color:var(--white)}
.footer-brand{position:absolute;left:0;top:70px;width:1200px;text-align:center}
.footer-brand .brand-name{color:var(--white);font-size:19px}
.footer-brand .brand-tag{color:var(--white)}
.call{position:absolute;left:0;top:136px;width:1200px;text-align:center;font-size:34px;font-weight:400}
.email{position:absolute;left:0;top:182px;width:1200px;text-align:center;font-size:14px}
.email b{color:var(--sky);font-weight:600}
.footer-rule{position:absolute;left:120px;top:244px;width:960px;height:1px;background:#3a72ad}
.social{position:absolute;left:580px;top:228px;width:34px;height:34px;border-radius:50%;background:var(--white)}
.legal{position:absolute;left:120px;top:292px;font-size:10.5px}
.legal b{color:var(--sky);font-weight:500}
.footer-links{position:absolute;left:443px;top:292px;font-size:10.5px;display:flex;gap:10px}
.footer-links .hl{color:var(--sky)}
.pay{position:absolute;left:913px;top:287px;display:flex;gap:6px}
.pay i{width:37px;height:23px;background:var(--white);border-radius:2px}
</style>
</head>
<body>

<header class="site-header">
  <a class="brand" href="#">
    <span class="brand-dot"></span>
    <span><span class="brand-name">HALVORN QUANTAX</span><span class="brand-tag" style="display:block">CONSTRUCTION TAKEOFF EXPERTS</span></span>
  </a>
  <nav class="main-nav">
    <a class="active" href="#">Home</a>
    <a href="#">Expertise</a>
    <a href="#">Takeoffs</a>
    <a href="#">Divisions Serviced</a>
  </nav>
  <a class="btn login" href="#">&#9786;&nbsp; Member Login</a>
</header>

<section class="hero">
  <div class="abs" role="img" aria-label="Dimmed photo of an excavator moving earth on a construction site" style="inset:0"></div>
  <svg class="slide-arrow" style="left:52px" width="18" height="18" viewBox="0 0 18 18" fill="none" stroke="#fff" stroke-width="2"><path d="M9 3 3 9l6 6M15 3 9 9l6 6"/></svg>
  <svg class="slide-arrow" style="left:1130px" width="18" height="18" viewBox="0 0 18 18" fill="none" stroke="#fff" stroke-width="2"><path d="M3 3l6 6-6 6M9 3l6 6-6 6"/></svg>
  <h1 class="hero-title">Time</h1>
  <p class="hero-sub">In Construction, Beyond Your Reputation, Nothing is More Valuable Than Your Time.</p>
  <form class="quote-form">
    <svg class="quote-head" width="256" height="88" viewBox="0 0 256 88"><path d="M0 0h256v62l-128 26L0 62z" fill="#0a4f96"/></svg>
    <div class="quote-head"><span>REGISTER FOR A<small>FREE QUOTE</small></span></div>
    <div class="field" style="top:98px">Name</div>
    <div class="field" style="top:138px">Company Name</div>
    <div class="field" style="top:178px">Phone</div>
    <div class="field" style="top:218px">Email</div>
    <span class="btn send">Send</span>
  </form>
</section>

<div class="about-photo" role="img" aria-label="Building wrapped in scaffolding against a blue sky"></div>
<h2 class="section-title left about-title">Halvorn Quantax</h2>
<div class="about-copy">
  <p>Dedicated to saving our clients time and money by specializing in accurate, reliable materials quantity calculations, Halvorn Quantax allows general contractors to confidently propose on more work with less stress.</p>
  <p>To receive a no-obligation answer to your takeoff needs complete the Request for Proposal form. Halvorn Quantax will provide a comprehensive proposal detailing the hours required ...</p>
</div>
<a class="btn discover" href="#">Discover More</a>

<section class="scopes">
  <h2 class="section-title center">Expert Takeoffs For all Scopes</h2>
  <svg class="abs" style="left:52px;top:183px" width="18" height="18" viewBox="0 0 18 18" fill="none" stroke="#fff" stroke-width="2"><path d="M9 3 3 9l6 6M15 3 9 9l6 6"/></svg>
  <svg class="abs" style="left:1130px;top:183px" width="18" height="18" viewBox="0 0 18 18" fill="none" stroke="#fff" stroke-width="2"><path d="M3 3l6 6-6 6M9 3l6 6-6 6"/></svg>

  <article class="scope" style="left:120px">
    <div class="scope-photo" role="img" aria-label="Painter working on a white porch railing" style="background:linear-gradient(135deg,#9dbbd6,#e9ecef)"></div>
    <h3>Painting</h3>
    <ul><li>Interior &amp; Exterior Paint</li><li>Breakouts by room &amp; finish schedule</li><li>Excel Spreadsheet &amp; Marked-up Plans</li></ul>
  </article>
  <a class="scope-link" style="left:120px" href="#">&#187; View Projects</a>

  <article class="scope" style="left:366px">
    <div class="scope-photo" role="img" aria-label="Modern office interior with built-in cabinetry" style="background:linear-gradient(135deg,#3b3f44,#d8d9da)"></div>
    <h3>Millwork</h3>
    <ul><li>Cabinets, Doors, Drawers</li><li>Sheathing, Underlayment, Flashing</li><li>Spreadsheet &amp; Marked-up Plans</li></ul>
  </article>
  <a class="scope-link" style="left:366px" href="#">&#187; View Projects</a>

  <article class="scope" style="left:614px">
    <div class="scope-photo" role="img" aria-label="Roofers installing roofing on a flat roof" style="background:linear-gradient(180deg,#5d9fe0,#c9c4bb)"></div>
    <h3>Roofing - Siding</h3>
    <ul><li>Shingles, Caps, Vents, Drip Edge</li><li>Sheathing, Underlayment, Flashing</li><li>Spreadsheet &amp; Marked-up Plans</li></ul>
  </article>
  <a class="scope-link" style="left:614px" href="#">&#187; Contact Us</a>

  <article class="scope" style="left:862px">
    <div class="scope-photo" role="img" aria-label="Workers finishing a wet concrete slab" style="background:linear-gradient(180deg,#8cb4d8,#6f7e86)"></div>
    <h3>Concrete - Foundation</h3>
    <ul><li>Pavement, Foundations, Side walks, Curbs</li><li>Rebar &amp; Membranes</li><li>Excel Spreadsheet &amp; Marked-up Plans</li></ul>
  </article>
  <a class="scope-link" style="left:862px" href="#">&#187; Contact Us</a>

  <a class="btn all-scopes" href="#">View All Scopes</a>
</section>

<h2 class="section-title center takeoffs-title">Takeoffs</h2>
<p class="takeoffs-lead">Construction is a complex, ever-changing challenge where seemingly no two days are the same</p>

<div class="step" style="left:170px">
  <svg width="44" height="44" viewBox="0 0 44 44" fill="none" stroke="#0a4f96" stroke-width="2.5" stroke-linejoin="round"><path d="M8 36l2-9 20-20 7 7-20 20zM26 11l7 7M10 27l7 7"/></svg>
  <h4>Request a Takeoff</h4>
  <p>To initiate a takeoff, clients complete a Request for Proposal to register their business and provide the project ...</p>
  <a class="read-more" href="#">&#187; Read More</a>
</div>
<div class="step" style="left:500px">
  <svg width="48" height="44" viewBox="0 0 48 44" fill="none" stroke="#f0a20c" stroke-width="2.5"><circle cx="18" cy="12" r="8"/><path d="M3 40c0-10 7-16 15-16 3 0 6 1 8 2"/><circle cx="36" cy="32" r="9"/><path d="M36 27v10M31 32h10"/></svg>
  <h4>Account Management</h4>
  <p>When a new client relationship is established, Halvorn Quantax will work with you to understand the specifics ...</p>
  <a class="read-more" style="color:var(--sky)" href="#">&#187; Read More</a>
</div>
<div class="step" style="left:830px">
  <svg width="30" height="44" viewBox="0 0 30 44" fill="none" stroke="#0a4f96" stroke-width="2.5"><path d="M15 3v38M24 12c-2-4-6-5-9-5-5 0-9 3-9 7 0 9 18 5 18 14 0 4-4 7-9 7-4 0-8-2-10-6"/></svg>
  <h4>Benefits</h4>
  <p>Time, money, and confidence combine to define the fundamental benefits Halvorn Quantax brings to every ...</p>
  <a class="read-more" href="#">&#187; Read More</a>
</div>

<section class="testimonial">
  <svg class="abs" style="left:572px;top:-10px" width="56" height="44" viewBox="0 0 56 44"><path d="M2 2h22v22L14 42H6l6-18H2zM32 2h22v22L44 42h-8l6-18H32z" fill="#fff"/></svg>
  <blockquote>Sometimes our work is super time sensitive and when I'm given unreasonable deadlines, Halvorn Quantax is my secret weapon. They are realistic in their assessments and when I say go, they never fail to deliver just what I want, just the way I want it!</blockquote>
  <div class="cite-name">Darren Pollard</div>
  <div class="cite-co">Meridian Builders, LLC.</div>
  <div class="dots"><i style="background:#fff"></i><i></i><i></i><i></i></div>
</section>

<h2 class="section-title center more-title">And Many, Many, More...</h2>
<p class="more-copy">Even if your scope is not listed here, give us a try! Our team of experts can handle almost any scope!</p>
<a class="btn register" href="#">Register Now!</a>

<footer class="site-footer">
  <div class="footer-brand">
    <div class="brand-name">HALVORN QUANTAX</div>
    <div class="brand-tag">CONSTRUCTION TAKEOFF EXPERTS</div>
  </div>
  <div class="call">Call Us: +1-555-014-2290</div>
  <div class="email"><b>Email:</b> info@halvornquantax.com</div>
  <div class="footer-rule"></div>
  <span class="social"></span>
  <div class="legal">© 2019 <b>Halvorn Quantax</b>. All Rights Reserved.</div>
  <nav class="footer-links"><a href="#">Become a Member</a><span>|</span><a class="hl" href="#">Privacy Policy</a><span>|</span><a href="#">Sitemap</a></nav>
  <div class="pay"><i></i><i></i><i></i><i style="background:#2f8fd1"></i></div>
</footer>

</body>
</html>
```